Luxury Candle Startup Needs Modern Packaging Box & Matching Label Design

We are Wickhollow, a luxury candle company about to launch in Australia and we need a box packaging design that is modern, minimalist, and feminine. Our target audience are females, mostly mothers, within the age range of 25-45 who are looking for high quality, handmade luxurious products. Our company is going to have a large social media presence with new mothers as we are going to show our journey with starting a business whilst on maternity leave. We would like the arch shape incorporated into the box packaging as it is beautiful and symbolises moving into a new phase in life which really represents the brand. We would like for the packaging box to be a simple white box with a sleeve insert over the box with the design to make printing easier. Our colour inspiration are very earthy colours and would like the sleeve colour to be easily changed according to the scent. For example dusky rose coloured sleeve for rose patchouli and amber scent, light coffee coloured sleeve for coffee bean cacao scent etc. Please see uploaded files for inspiration, our logo, and the type of candle jars used.
The box dimensions are:
External Dimension: 95mmW x 95mmL x 116mmH
We look forward to seeing your amazing designs!

```html
<!DOCTYPE html>
<html lang="en">
<head>
<meta charset="utf-8">
<title>Wickhollow – Candle Box Sleeve</title>
<link href="https://fonts.googleapis.com/css2?family=Italiana&family=Montserrat:wght@400;500&display=swap" rel="stylesheet">
<style>
  :root {
    --backdrop: #f3f1f0;
    --sleeve-front: #bd9dc7;
    --sleeve-side: #b17d88;
    --box-white: #f1f1f3;
    --box-shade: #e2e0e2;
    --pattern-deep: #8d6fa6;
    --pattern-mid: #c9a9c8;
    --pattern-light: #e8cfd4;
    --ink-light: #fbf6f8;
  }
  html, body {
    margin: 0;
    padding: 0;
    width: 1200px;
    height: 1092px;
    overflow: hidden;
    background: var(--backdrop);
  }
  .canvas {
    position: relative;
    width: 1200px;
    height: 1092px;
  }
  .dieline {
    position: absolute;
    left: 160px;
    top: 278px;
    width: 880px;
    height: 536px;
    display: flex;
  }
  .panel {
    position: relative;
    width: 440px;
    height: 536px;
  }
  .sleeve {
    position: absolute;
    left: 0;
    top: 0;
    width: 100%;
    height: 375px;
  }
  .panel--side .sleeve { background: var(--sleeve-side); }
  .panel--front .sleeve { background: var(--sleeve-front); }
  .box-base {
    position: absolute;
    left: 0;
    bottom: 0;
    width: 100%;
    height: 161px;
    background: var(--box-white);
  }
  .panel--side .box-base { background: var(--box-shade); }
  .web-address {
    position: absolute;
    left: 48px;
    bottom: 40px;
    font-family: 'Montserrat', sans-serif;
    font-size: 12px;
    letter-spacing: 1px;
    color: var(--ink-light);
    opacity: 0.85;
  }
  .pattern-window {
    position: absolute;
    left: 94px;
    top: 0;
    width: 252px;
    height: 222px;
    display: block;
  }
  .wordmark {
    position: absolute;
    left: 0;
    top: 234px;
    width: 100%;
    margin: 0;
    text-align: center;
    font-family: 'Italiana', serif;
    font-weight: 400;
    font-size: 54px;
    letter-spacing: 2px;
    color: var(--ink-light);
    line-height: 1;
  }
  .tagline {
    position: absolute;
    left: 0;
    width: 100%;
    margin: 0;
    text-align: center;
    font-family: 'Montserrat', sans-serif;
    font-weight: 500;
    color: var(--ink-light);
  }
  .tagline--main { top: 300px; font-size: 11px; letter-spacing: 2.5px; }
  .tagline--origin { top: 324px; font-size: 8px; letter-spacing: 2.5px; }
  .pull-tab {
    position: absolute;
    left: 208px;
    top: 375px;
    width: 24px;
    height: 30px;
    background: #ffffff;
    border-radius: 0 0 3px 3px;
    box-shadow: 0 1px 2px rgba(0,0,0,0.12);
  }
</style>
</head>
<body>
<main class="canvas">
  <div class="dieline">
    <section class="panel panel--side">
      <div class="sleeve">
        <p class="web-address">www.wickhollow.com.au</p>
      </div>
      <div class="box-base"></div>
    </section>
    <section class="panel panel--front">
      <div class="sleeve">
        <svg class="pattern-window" viewBox="0 0 252 222" role="img" aria-label="Floral pattern of lilac and blush blooms with cream centres and soft leaves">
          <defs>
            <linearGradient id="floralTone" x1="0" y1="0" x2="1" y2="1">
              <stop offset="0" stop-color="#d9b8c2"/>
              <stop offset="0.5" stop-color="#b594bd"/>
              <stop offset="1" stop-color="#8d6fa6"/>
            </linearGradient>
          </defs>
          <rect width="252" height="222" fill="url(#floralTone)"/>
        </svg>
        <h1 class="wordmark">WICKHOLLOW</h1>
        <p class="tagline tagline--main">LUXURY FRAGRANCE</p>
        <p class="tagline tagline--origin">AUSTRALIA</p>
      </div>
      <div class="box-base"></div>
      <div class="pull-tab"></div>
    </section>
  </div>
</main>
</body>
</html>
```